Gritty, Modern True Crime Podcast Launch

Launching a new true crime podcast and are looking for some designs. We are targeting the color scheme of black and red and are looking for both a "noir" and modern vibe. Here is a great example of a current podcast (and look) we love: http://quarrelcast-example.net.The podcast name we like is "Hollow Crows." We'd love to go with a rat image (or group of rats) along with some stylized text. Both examples are attached below.

Font styles to use
Serif
Sans Serif

Colors
ec1f27
000000
ffffff
f04a50
1b1b1b

Requirements
Must have
• Rat in design, stylized text, incorporation of primarily red and black colors
Should not have
• photorealistic rats

```html
<!DOCTYPE html>
<html lang="en">
<head>
<meta charset="utf-8">
<title>Hollow Crows – Podcast Artwork and Player</title>
<link href="https://fonts.googleapis.com/css2?family=Black+Ops+One&family=Lato:wght@400;700&display=swap" rel="stylesheet">
<style>
  :root {
    --stage: #e4e4e4;
    --red: #ec1f27;
    --red-deep: #a8121a;
    --black: #000000;
    --ink: #1b1b1b;
    --white: #ffffff;
    --rat-pale: #e8b4b8;
    --rat-shade: #c98a90;
    --tail: #a9a6a0;
    --panel: #262f37;
    --panel-line: #323c45;
    --muted: #9aa3aa;
    --track: #3a454f;
    --accent: #1e8fe0;
  }
  * { box-sizing: border-box; margin: 0; padding: 0; }
  html, body { width: 1200px; height: 675px; overflow: hidden; }
  body { background: var(--stage); position: relative; font-family: "Lato", Arial, sans-serif; }

  .cover { position: absolute; overflow: hidden; background: var(--red); }
  .cover-large { left: 177px; top: 114px; width: 446px; height: 446px; }
  .cover-background {
    position: absolute; inset: 0;
    background:
      radial-gradient(ellipse 30% 14% at 8% 2%, rgba(0,0,0,0.85), rgba(0,0,0,0) 100%),
      radial-gradient(ellipse 26% 14% at 100% 100%, rgba(0,0,0,0.9), rgba(0,0,0,0) 100%),
      linear-gradient(160deg, #d8161e, #c8151c 55%, #a3111a);
  }
  .cover-illustration {
    position: absolute; left: 36%; top: 4%; width: 56%; height: 92%;
    border-radius: 48% 52% 40% 40% / 30% 30% 60% 60%;
    background: radial-gradient(ellipse 60% 55% at 55% 40%, var(--rat-pale), var(--rat-shade) 70%, rgba(201,138,144,0.35) 100%);
    opacity: 0.9;
  }
  .cover-title {
    position: absolute; left: 0; right: 0;
    font-family: "Black Ops One", "Arial Black", sans-serif;
    color: var(--black); text-align: center; line-height: 1;
  }
  .cover-large .title-top { top: 243px; font-size: 62px; }
  .cover-large .title-bottom { top: 306px; font-size: 92px; }

  .player { position: absolute; left: 676px; top: 29px; width: 347px; height: 617px; background: var(--panel); color: var(--white); }
  .status-bar { position: absolute; top: 5px; left: 7px; right: 7px; height: 16px; font-size: 12px; display: flex; align-items: center; }
  .status-left { display: flex; align-items: center; gap: 4px; flex: 1; }
  .status-time { flex: 1; text-align: center; }
  .status-right { flex: 1; display: flex; justify-content: flex-end; align-items: center; gap: 4px; }
  .nav-bar { position: absolute; top: 32px; left: 0; right: 0; height: 24px; }
  .nav-title { text-align: center; font-size: 16px; line-height: 24px; }
  .nav-back { position: absolute; left: 18px; top: 4px; }
  .nav-search { position: absolute; right: 18px; top: 4px; }

  .cover-small { left: 74px; top: 92px; width: 195px; height: 197px; }
  .cover-small .title-top { top: 106px; font-size: 27px; }
  .cover-small .title-bottom { top: 134px; font-size: 40px; }

  .track-info { position: absolute; top: 311px; left: 0; right: 0; text-align: center; }
  .track-genre { font-size: 9.5px; color: var(--muted); }
  .track-name { font-size: 16.5px; font-weight: 700; margin-top: 9px; }
  .track-meta { font-size: 9.5px; color: #c3c9ce; margin-top: 9px; }

  .divider { position: absolute; left: 0; right: 0; height: 1px; background: var(--panel-line); }

  .transport { position: absolute; left: 0; right: 0; top: 424px; height: 60px; }
  .transport svg { position: absolute; }

  .progress { position: absolute; left: 22px; width: 303px; top: 508px; height: 5px; border-radius: 3px; background: var(--track); }
  .progress-fill { width: 196px; height: 100%; border-radius: 3px; background: var(--accent); }
  .progress-handle { position: absolute; left: 195px; top: -3px; width: 3px; height: 11px; background: var(--white); }
  .time { position: absolute; top: 530px; font-size: 10px; }
  .time-elapsed { left: 21px; }
  .time-total { right: 22px; }

  .bottom-row svg { position: absolute; }
  .volume { position: absolute; left: 106px; top: 587px; width: 164px; height: 5px; border-radius: 3px; background: var(--track); }
  .volume-fill { width: 65px; height: 100%; border-radius: 3px; background: var(--accent); }
  .volume-knob { position: absolute; left: 59px; top: -3px; width: 11px; height: 11px; border-radius: 50%; background: var(--white); }
</style>
</head>
<body>

<section class="cover cover-large">
  <div class="cover-background"></div>
  <div class="cover-illustration" role="img" aria-label="Illustration area: pale stylized rat rearing up on its hind legs, mouth open, tail curling below the title"></div>
  <div class="cover-title title-top">HOLLOW</div>
  <div class="cover-title title-bottom">CROWS</div>
</section>

<section class="player">
  <div class="status-bar">
    <div class="status-left">
      <svg width="30" height="7" viewBox="0 0 30 7"><g fill="#fff"><circle cx="3" cy="3.5" r="3"/><circle cx="9.5" cy="3.5" r="3"/><circle cx="16" cy="3.5" r="3"/><circle cx="22.5" cy="3.5" r="3"/></g><circle cx="27" cy="3.5" r="2.5" fill="none" stroke="#fff" stroke-width="0.8"/></svg>
      <span>VERA</span>
      <svg width="13" height="10" viewBox="0 0 13 10"><path d="M1 3.5a8 8 0 0 1 11 0M3 5.5a5 5 0 0 1 7 0M5 7.5a2 2 0 0 1 3 0" fill="none" stroke="#fff" stroke-width="1.3"/><circle cx="6.5" cy="9" r="0.9" fill="#fff"/></svg>
    </div>
    <div class="status-time">4:21 PM</div>
    <div class="status-right">
      <svg width="7" height="11" viewBox="0 0 7 11"><path d="M1 3l5 5-2.5 2V1L6 3 1 8" fill="none" stroke="#8a949c" stroke-width="0.9"/></svg>
      <span>22%</span>
      <svg width="26" height="11" viewBox="0 0 26 11"><rect x="0.5" y="0.5" width="22" height="10" rx="2" fill="none" stroke="#fff"/><rect x="2" y="2" width="4" height="7" fill="#fff"/><rect x="23.5" y="3.5" width="1.5" height="4" fill="#fff"/></svg>
    </div>
  </div>

  <div class="nav-bar">
    <svg class="nav-back" width="10" height="16" viewBox="0 0 10 16"><path d="M8 1L1 8l7 7" fill="none" stroke="#fff" stroke-width="1.5"/></svg>
    <div class="nav-title">Now Playing</div>
    <svg class="nav-search" width="16" height="16" viewBox="0 0 16 16"><circle cx="6.5" cy="6.5" r="5.5" fill="none" stroke="#fff" stroke-width="1.4"/><path d="M10.5 10.5L15 15" stroke="#fff" stroke-width="1.5"/></svg>
  </div>

  <div class="cover cover-small">
    <div class="cover-background"></div>
    <div class="cover-illustration" role="img" aria-label="Podcast cover illustration area: pale stylized rat rearing up on a grungy red background"></div>
    <div class="cover-title title-top">HOLLOW</div>
    <div class="cover-title title-bottom">CROWS</div>
  </div>

  <div class="track-info">
    <p class="track-genre">Gritty, Modern True Crime Podcast</p>
    <p class="track-name">Hollow Crows - True Crime Podcast</p>
    <p class="track-meta">Some Information Here</p>
  </div>

  <div class="divider" style="top:402px"></div>

  <div class="transport">
    <svg style="left:101px;top:20px" width="22" height="18" viewBox="0 0 22 18"><path d="M11 1L1 9l10 8zM21 1L11 9l10 8z" fill="#fff"/></svg>
    <svg style="left:143px;top:0" width="60" height="60" viewBox="0 0 60 60"><circle cx="30" cy="30" r="28.5" fill="none" stroke="#fff" stroke-width="1.6"/><path d="M24 19v22l18-11z" fill="#fff"/></svg>
    <svg style="left:224px;top:20px" width="22" height="18" viewBox="0 0 22 18"><path d="M1 1l10 8-10 8zM11 1l10 8-10 8z" fill="#fff"/></svg>
  </div>

  <div class="progress"><div class="progress-fill"></div><div class="progress-handle"></div></div>
  <div class="time time-elapsed">31:14</div>
  <div class="time time-total">45:00</div>

  <div class="divider" style="top:561px"></div>

  <div class="bottom-row">
    <svg style="left:21px;top:583px" width="18" height="12" viewBox="0 0 18 12"><path d="M1 3h4l7 6h4M1 9h4l7-6h4M14 1l2.5 2L14 5M14 7l2.5 2L14 11" fill="none" stroke="#1e8fe0" stroke-width="1.6"/></svg>
    <svg style="left:78px;top:583px" width="15" height="12" viewBox="0 0 15 12"><path d="M1 4h3l4-3v10L4 8H1z" fill="#fff"/><path d="M10 3.5a3 3 0 0 1 0 5M12 1.5a6 6 0 0 1 0 9" fill="none" stroke="#fff" stroke-width="1.2"/></svg>
    <div class="volume"><div class="volume-fill"></div><div class="volume-knob"></div></div>
    <svg style="left:313px;top:583px" width="13" height="13" viewBox="0 0 13 13"><path d="M11 6.5A4.5 4.5 0 1 1 8.5 2.4" fill="none" stroke="#fff" stroke-width="1.5"/><path d="M7 0.5l3.5 2-3 2.5z" fill="#fff"/></svg>
  </div>
</section>

</body>
</html>
```